Prairie Pete''s Funhouse Website Revamp

We have a children's entertainment center that hasn't changed in 20 years and the site looks like it was created 20 years ago. We need a new, modern, clean site that pops. Attached is the new logo that should be used as a style guide.

Current site is: www.prairiepetesfun.example

Thanks!
Updates

Designers, thank you all for the amazing work. It was exciting to be able to go through and see all the creativity that came in. I have decided on a design but wanted to share my thanks and appreciation for your time. Warm regards, Colton

Target Market(s)

Mothers with children in the 2 - 14 range.

Industry/Entity Type

Entertainment

```html
<!DOCTYPE html>
<html lang="en">
<head>
<meta charset="utf-8">
<title>Prairie Pete's Funhouse</title>
<link rel="stylesheet" href="https://fonts.googleapis.com/css2?family=Varela+Round&family=Open+Sans:wght@400;600&display=swap">
<style>
:root{
  --sky-top:#3fb0ee;
  --sky-mid:#9fdcf7;
  --orange:#f47f1f;
  --orange-dark:#e56a10;
  --teal:#22c6cf;
  --teal-dark:#17a9b5;
  --heading-orange:#ef6a1f;
  --red:#c8102e;
  --green-text:#5aa51c;
  --teal-text:#1fb5bd;
  --body:#555;
  --footer:#8aae27;
  --footer-bottom:#a0c03e;
  --border:#dcdcdc;
  --white:#fff;
}
*{box-sizing:border-box;margin:0;padding:0}
html,body{width:918px;height:1200px;overflow:hidden}
body{position:relative;background:var(--white);font-family:"Open Sans",sans-serif;color:var(--body)}
.sky{position:absolute;left:0;top:0;width:918px;height:520px;background:linear-gradient(180deg,var(--sky-top) 0%,var(--sky-mid) 40%,#e9f7fd 70%,#fff 100%)}
.art-left{position:absolute;left:0;top:0;width:90px;height:490px;background:linear-gradient(180deg,#4a9b2a 0%,#8a6a4a 30%,#d8d8d8 55%,#e8a23c 80%,rgba(255,255,255,0) 100%)}
.art-right{position:absolute;right:0;top:0;width:86px;height:490px;background:linear-gradient(180deg,#3e9a2a 0%,#f0b640 35%,#6fb83a 60%,#f2c9a0 80%,rgba(255,255,255,0) 100%)}
.nav{position:absolute;left:76px;top:72px;width:766px;height:50px;background:linear-gradient(180deg,#f99a3c,var(--orange) 60%,var(--orange-dark));border:2px solid #fff;border-bottom:none;border-radius:6px 6px 0 0}
.nav a{position:absolute;top:0;height:48px;line-height:48px;color:#fff;text-decoration:none;font-family:"Varela Round",sans-serif;font-size:13.5px;text-align:center;border-right:1px solid rgba(255,255,255,.35)}
.nav a.last{border-right:none}
.nav a.right{border-right:none;border-left:1px solid rgba(255,255,255,.35)}
.logo{position:absolute;left:342px;top:32px;width:232px;height:120px;border-radius:50%;background:#fff;border:4px solid #cfeefa;display:flex;align-items:center;justify-content:center;text-align:center;gap:6px}
.logo-mark{width:14px;height:14px;border-radius:50%;background:var(--orange)}
.logo-name{font-family:"Varela Round",sans-serif;font-size:19px;line-height:1.15;color:#2b9a3c}
.hero{position:absolute;left:76px;top:120px;width:766px;height:340px}
.hero-text{position:absolute;left:126px;top:200px;color:#fff}
.hero-kicker{font-family:"Varela Round",sans-serif;font-size:22px}
.hero-title{font-family:"Varela Round",sans-serif;font-size:30px;margin-top:2px}
.hero-copy{font-size:10.5px;line-height:16px;width:330px;margin-top:8px}
.dots{display:flex;gap:3px;margin-top:10px;margin-left:2px}
.dots span{width:9px;height:9px;border-radius:50%;background:rgba(255,255,255,.55)}
.dots span.on{background:#fff}
.hero-photo{position:absolute;left:480px;top:158px;width:324px;height:243px;background:#6a8a1f;padding:16px}
.hero-photo div{width:100%;height:100%;background:linear-gradient(160deg,#c9842a,#8a3a1c 45%,#3a2a20 75%,#d9cfc2)}
.welcome{position:absolute;left:120px;top:492px;width:678px;text-align:center}
.welcome h1{font-family:"Varela Round",sans-serif;font-weight:400;font-size:25px;color:var(--heading-orange);margin-bottom:12px}
.welcome p{font-size:10px;line-height:16.5px;margin-bottom:4px}
.card{position:absolute;top:636px;width:247px;height:250px;border:1px solid var(--border);border-radius:4px;background:#fff;padding:18px 20px}
.card h2{font-family:"Varela Round",sans-serif;font-weight:400;font-size:18px;line-height:22px;margin-bottom:12px}
.offers h2{color:var(--red)}
.drive h2{color:var(--green-text)}
.ideal h2{color:var(--teal-text)}
.offer-art{width:207px;height:93px;border-radius:4px;background:linear-gradient(135deg,#8fd24e,#3aa52a)}
.card p{font-size:9.5px;line-height:16.5px;margin-top:8px;padding:0 3px}
.btn{display:inline-block;margin:8px 3px 0;width:93px;height:28px;line-height:28px;text-align:center;background:linear-gradient(180deg,#d8263c,var(--red));color:#fff;font-size:9.5px;border-radius:3px;text-decoration:none}
.drive ul{list-style:none;font-size:9.5px;line-height:22.4px;padding-left:2px}
.ideal ul{list-style:none;font-size:9.5px;line-height:20.2px;padding-left:4px}
.ideal li::before{content:"";display:inline-block;width:0;height:0;border-left:4px solid #bbb;border-top:3px solid transparent;border-bottom:3px solid transparent;margin-right:10px;vertical-align:1px}
.footer{position:absolute;left:0;top:950px;width:918px;height:198px;background:var(--footer);border-top:4px solid #9ac43a}
.footer h3{position:absolute;top:32px;font-weight:600;font-size:13.5px;color:#fff}
.footer ul{position:absolute;list-style:none;top:58px;font-size:9.5px;line-height:20px;color:#fff;text-transform:uppercase}
.social{position:absolute;left:536px;top:60px;display:flex;gap:8px}
.social span{width:19px;height:19px;border-radius:3px;background:rgba(255,255,255,.85)}
.legal{position:absolute;left:0;top:1148px;width:918px;height:52px;background:var(--footer-bottom);color:#fff;font-size:8.5px;padding:19px 0 0 80px}
</style>
</head>
<body>
<div class="sky"></div>
<div class="art-left" role="img" aria-label="Cartoon jungle animals and leaves along the left edge"></div>
<div class="art-right" role="img" aria-label="Cartoon jungle animals and leaves along the right edge"></div>

<nav class="nav">
  <a href="#" style="left:0;width:77px">Home</a>
  <a href="#" style="left:77px;width:94px">Attraction</a>
  <a href="#" class="last" style="left:171px;width:72px">Parties</a>
  <a href="#" class="right" style="left:503px;width:86px">Pricing</a>
  <a href="#" class="right" style="left:589px;width:89px">Directions</a>
  <a href="#" class="right" style="left:678px;width:86px">Contact</a>
</nav>

<section class="hero">
  <svg width="766" height="340" viewBox="0 0 766 340" style="position:absolute;left:0;top:0">
    <defs>
      <linearGradient id="teal" x1="0" y1="0" x2="0" y2="1">
        <stop offset="0" stop-color="#25cdd5"/>
        <stop offset="1" stop-color="#12a7b4"/>
      </linearGradient>
    </defs>
    <path d="M2 0 H764 V302 Q383 336 2 302 Z" fill="url(#teal)" stroke="#fff" stroke-width="5"/>
  </svg>
</section>

<div class="logo"><span class="logo-mark"></span><span class="logo-name">Prairie Pete's<br>Funhouse</span></div>

<div class="hero-text">
  <div class="hero-kicker">Mauris vel lacus vitae</div>
  <div class="hero-title">Donec convallis pede</div>
  <p class="hero-copy">Maecenas at justo id velit placerat molestie Donec dictum lectus non odio Cras a ante vitae enim iaculis aliqu</p>
  <div class="dots"><span class="on"></span><span></span><span></span><span></span></div>
</div>
<div class="hero-photo"><div role="img" aria-label="Photo of children riding an indoor carousel"></div></div>

<section class="welcome">
  <h1>Welcome to Our Website Mainpage</h1>
  <p>Prairie Pete's Funhouse is the Wasatch Fronts #1 indoor amusement park for young kids. We cater exclusively to children from infants to around 11 years old.&nbsp;&nbsp; Our climate controlled fun center offers a unique mix of seven different amusement park rides.</p>
  <p>Prairie Pete's also makes its own pizza with fresh ingredients that will satisfy any families appetite. Our family fun center is a fun, affordable and exciting birthday party place. Check out our birthday party packages or use your own birthday party ideas.</p>
</section>

<article class="card offers" style="left:76px">
  <h2>Online Offers</h2>
  <div class="offer-art" role="img" aria-label="Illustration of gold coins on green banknotes"></div>
  <p>Maecenas at justo id velit placerat molestie Donec dictum lectus non odio Cras a ante vitae enim iaculis aliquam</p>
  <a class="btn" href="#">CLICK HERE</a>
</article>

<article class="card drive" style="left:336px">
  <h2>Driving distance to<br>Prairie Pete's:</h2>
  <ul>
    <li>Salt Lake City,Utah 8mi: Murray,Utah 3mi:</li>
    <li>Draper,Utah 8mi: Sandy,Utah 3mi:</li>
    <li>Riverton,Utah 9mi: South Jordan,Utah 10mi:</li>
    <li>West Jordan,Utah 6mi: Holladay,Utah 5mi:</li>
    <li>Cottonwood Heights,Utah 3mi:</li>
    <li>Taylorsville,Utah 8mi: West Valley City,Utah</li>
    <li>12mi: Bountiful,Utah 23mi: Farmington,Utah</li>
  </ul>
</article>

<article class="card ideal" style="left:595px">
  <h2>Prairie Pete's is ideal for</h2>
  <ul>
    <li>Kids Birthday Parties</li>
    <li>Play Group Location</li>
    <li>Family Night Activities</li>
    <li>Kids Field Trip Location</li>
    <li>Grandparents Day Out with the Kids</li>
    <li>Fun things to do with Kids</li>
    <li>Large Groups and Large Parties</li>
    <li>Off Track Activities for Children</li>
    <li>Rainy Day Activities</li>
  </ul>
</article>

<footer class="footer">
  <h3 style="left:81px">QUICK LINKS</h3>
  <ul style="left:83px"><li>Home Page</li><li>The Prairie Cafe</li><li>Attractions</li><li>Parties</li></ul>
  <ul style="left:209px"><li>Pricing</li><li>Group Outings</li><li>Directions</li><li>Contact Us</li></ul>
  <h3 style="left:349px">CONTACT US</h3>
  <ul style="left:352px"><li>412 W. Meadowlark</li><li>Avenue</li><li>In Riverdale, Utah</li><li>Call 555-014-2273</li></ul>
  <h3 style="left:536px">GET IN TOUCH</h3>
  <div class="social"><span></span><span></span><span></span><span></span></div>
</footer>
<div class="legal">© 2014 Company Name&nbsp; All right reserved&nbsp; Term of Use</div>
</body>
</html>
```